Website design: Mobile Physiotherapy, Massage & Personal Training Business

I need a website that reflects a staff of health and fitness professionals. I would like the theme of the website to match the company logo (Summit Motion Wellness).
This is a link for a competitors website that I am fond of:
http://www.brackenrehab.com.au/
I am open to any and all creative and innovative designs.

```html
<!DOCTYPE html>
<html lang="en">
<head>
<meta charset="utf-8">
<title>Summit Motion Wellness</title>
<link href="https://fonts.googleapis.com/css2?family=Open+Sans:ital,wght@0,400;0,600;0,700;1,400;1,600;1,700&display=swap" rel="stylesheet">
<style>
:root{
  --red:#b81e24;
  --red-dark:#a01a1f;
  --ink:#222;
  --text:#555;
  --muted:#888;
  --nav:#1d1d1d;
  --footer:#2a2a2a;
  --grey-panel:#d4d4d4;
  --line:#ddd;
  --white:#fff;
}
*{box-sizing:border-box;margin:0;padding:0}
html,body{width:800px;height:1200px;overflow:hidden;background:var(--white)}
body{position:relative;font-family:"Open Sans",Arial,sans-serif;color:var(--text)}
.abs{position:absolute}
.top-rule{left:0;top:0;width:800px;height:2px;background:var(--red)}

/* header */
.brand{left:67px;top:18px;display:flex;align-items:center;gap:7px}
.brand-mark{width:14px;height:14px;border-radius:50%;background:var(--red)}
.brand-name{font-size:17px;font-weight:700;color:var(--red);letter-spacing:-.2px}
.brand-tag{left:67px;top:58px;font-size:5px;font-weight:700;color:var(--ink);letter-spacing:.1px}
.phone{left:445px;top:24px;display:flex;align-items:center;gap:10px}
.phone-sep{width:1px;height:28px;background:var(--line)}
.phone-nums{font-size:9px;color:var(--muted);line-height:13px}
.btn{height:17px;font-size:9px;font-weight:600;color:var(--white);display:flex;align-items:center;justify-content:center}
.btn-register{left:605px;top:20px;width:60px;background:var(--nav)}
.btn-login{left:673px;top:20px;width:61px;background:var(--red)}
.search{left:570px;top:44px;width:164px;height:18px;background:#eee;display:flex;justify-content:flex-end}
.search-go{width:22px;height:18px;background:#333;display:flex;align-items:center;justify-content:center}

.nav{left:67px;top:82px;width:667px;height:36px;display:flex;background:var(--nav)}
.nav a{flex:1;display:flex;align-items:center;justify-content:center;color:var(--white);font-size:10px;text-decoration:none;border-left:1px solid #555}
.nav a:first-child{border-left:0;background:var(--red)}

/* hero */
.hero{left:67px;top:131px;width:667px;height:293px;background:linear-gradient(90deg,#c79a84 0%,#e9b59d 30%,#f2c3a7 55%,#e79a7d 85%,#a8786b 100%)}
.hero-title{left:504px;top:217px;font-size:14px;color:var(--red)}
.hero-copy{left:486px;top:246px;width:196px;font-size:7.5px;font-weight:600;color:var(--ink);text-align:right;line-height:12.4px}
.hero-btn{left:608px;top:326px;width:73px;height:17px;background:var(--red);color:var(--white);font-size:8.5px;font-weight:600;display:flex;align-items:center;justify-content:center;box-shadow:0 2px 2px rgba(0,0,0,.25)}
.hero-arrow{width:18px;height:18px;border-radius:50%;background:rgba(255,255,255,.5);display:flex;align-items:center;justify-content:center}

/* welcome */
.h-section{font-size:12px;color:var(--red);font-weight:400}
.welcome-title{left:66px;top:446px}
.welcome-figure{left:67px;top:478px;width:80px;height:129px;background:linear-gradient(180deg,#e8d6cc,#5bb6d6 45%,#c2393a 62%,#7d8594 85%)}
.welcome-copy{left:163px;top:480px;width:322px;font-size:8px;line-height:12.6px;text-align:justify}
.welcome-copy2{left:148px;top:563px;width:337px;font-size:8px;line-height:12.6px;text-align:justify}
.video{left:502px;top:449px;width:230px;height:148px;background:linear-gradient(135deg,#333 0%,#1a1a1a 55%,#5a2a2a 100%);display:flex;align-items:center;justify-content:center}
.play{width:26px;height:26px;border-radius:50%;background:var(--red);display:flex;align-items:center;justify-content:center}

/* columns */
.col-title{top:656px;font-size:12px;text-align:center}
.mini-arrow{width:10px;height:10px;background:#bbb;display:flex;align-items:center;justify-content:center}
.mini-arrow.red{background:var(--red)}
.trainer{top:688px;width:80px;text-align:center}
.trainer-photo{width:46px;height:46px;border-radius:50%;margin:0 auto 18px;background:linear-gradient(180deg,#b89075,#6e5446)}
.trainer-name{font-size:7.5px;font-weight:700;color:var(--ink)}
.trainer-role{font-size:6px;font-style:italic;color:var(--red)}
.trainer-quote{font-size:6px;font-style:italic;color:var(--text);margin-top:5px;line-height:8px}
.trainer-icons{display:flex;justify-content:space-between;padding:0 4px;margin-top:6px}
.trainer-divider{left:172px;top:690px;width:1px;height:110px;background:#cde6f2}

.events{left:295px;top:681px;width:211px;height:143px;background:var(--red);color:var(--white)}
.event{position:absolute;left:15px;width:185px}
.event-date{font-size:9px;font-weight:700}
.event-photo{position:absolute;top:14px;left:1px;width:69px;height:40px;background:linear-gradient(135deg,#e8e2dc,#9c8a80)}
.event-time{position:absolute;left:105px;top:0;font-size:5.5px;font-weight:700}
.event-name{position:absolute;left:99px;top:8px;font-size:9.5px;color:#7a1013}
.event-text{position:absolute;left:92px;top:22px;width:100px;font-size:6px;line-height:8px}
.event-book{position:absolute;left:100px;top:43px;width:49px;height:10px;border:1px solid var(--white);font-size:5px;font-weight:700;display:flex;align-items:center;justify-content:center;background:#8e1418}
.event-rule{position:absolute;left:20px;top:70px;width:171px;height:1px;background:rgba(255,255,255,.45)}

.blog{left:523px;top:681px;width:212px;height:143px;background:var(--grey-panel)}
.blog-item{position:absolute;left:12px;width:190px;height:40px}
.blog-thumb{position:absolute;left:0;top:0;width:40px;height:40px}
.blog-text{position:absolute;left:50px;top:3px;width:145px;font-size:7px;line-height:10px;color:#444}
.blog-date{font-size:6.5px;color:var(--muted);margin-top:1px}

/* partners */
.partners-title{left:0;width:800px;top:871px;text-align:center}
.partner{top:904px;width:93px;height:55px;border:1px solid var(--line);display:flex;align-items:center;justify-content:center}

/* footer */
.footer{left:0;top:993px;width:800px;height:178px;background:var(--footer)}
.f-head{font-size:10.5px;color:var(--white)}
.f-small{font-size:7.5px;color:#999;line-height:10.5px}
.f-input{left:68px;top:1082px;width:199px;height:22px;background:#6b6b6b;border:1px solid var(--red);color:#ddd;font-size:7px;display:flex;align-items:center;padding-left:13px}
.f-submit{left:68px;top:1113px;width:126px;height:21px;background:var(--red);color:var(--white);font-size:7px;display:flex;align-items:center;justify-content:space-between;padding:0 12px}
.f-brand{left:358px;top:1013px;display:flex;align-items:center;gap:6px}
.f-brand .brand-name{color:var(--white);font-size:13px}
.f-brand .brand-mark{background:var(--white);width:10px;height:10px}
.f-copy{left:303px;top:1053px;width:220px;font-size:7.5px;color:#999;line-height:11.5px}
.f-contact{left:303px;font-size:7.5px;color:var(--white);display:flex;align-items:center}
.f-contact b{font-size:11px;font-style:italic;font-weight:600;margin-left:12px}
.f-list{list-style:none;font-size:7.5px;color:#999;line-height:14px}
.f-list li::before{content:"›";margin-right:7px;color:#ccc}
.bottom-bar{left:0;top:1171px;width:800px;height:29px;background:var(--red)}
.bottom-copy{left:66px;top:1180px;font-size:7.5px;color:var(--white)}
.social{left:628px;top:1182px;display:flex;gap:9px}
.social span{width:7px;height:7px;border-radius:50%;background:#e7a3a6}
</style>
</head>
<body>
<div class="abs top-rule"></div>

<header>
  <div class="abs brand"><span class="brand-mark"></span><span class="brand-name">Summit Motion Wellness</span></div>
  <div class="abs brand-tag">MOBILE PHYSIOTHERAPY, MASSAGE AND PERSONAL TRAINING</div>
  <div class="abs phone">
    <svg width="18" height="24" viewBox="0 0 18 24"><path d="M4 2 L8 2 L9 8 L6 10 Q8 15 12 18 L14 15 L18 17 L17 22 Q14 24 10 21 Q3 15 2 7 Q2 3 4 2Z" fill="#b81e24"/></svg>
    <span class="phone-sep"></span>
    <div class="phone-nums">071-4402816<br>071-4402816</div>
  </div>
  <div class="abs btn btn-register">Register</div>
  <div class="abs btn btn-login">Login</div>
  <div class="abs search"><div class="search-go"><svg width="9" height="9" viewBox="0 0 9 9"><circle cx="3.7" cy="3.7" r="2.7" fill="none" stroke="#fff" stroke-width="1.2"/><line x1="5.7" y1="5.7" x2="8.4" y2="8.4" stroke="#fff" stroke-width="1.3"/></svg></div></div>
  <nav class="abs nav">
    <a>HOME</a><a>ABOUT US</a><a>SERVICES</a><a>PRODUCTS</a><a>FAQ</a><a>CONTACTS US</a><a>NEWS</a><a>EXTRAS</a>
  </nav>
</header>

<section>
  <div class="abs hero" role="img" aria-label="Photo of a woman running outdoors at sunset"></div>
  <div class="abs hero-arrow" style="left:82px;top:261px"><svg width="8" height="8" viewBox="0 0 8 8"><path d="M5.5 1 L2.5 4 L5.5 7" fill="none" stroke="#b81e24" stroke-width="1.6"/></svg></div>
  <div class="abs hero-arrow" style="left:701px;top:261px"><svg width="8" height="8" viewBox="0 0 8 8"><path d="M2.5 1 L5.5 4 L2.5 7" fill="none" stroke="#fff" stroke-width="1.6"/></svg></div>
  <h1 class="abs hero-title" style="font-weight:400">Lorem ipsum dolor sit amet</h1>
  <p class="abs hero-copy">Consectetur adipiscing elit. Donec nec scelerisque velit. Nullam id pharetra ligula. Aenean rutrum fermentum tortor vel gravida. Vivamus tincidunt sapien sit amet hendrerit scelerisque. Nunc urna lacus, mattis et mattis et, vestibulum et tortor. In</p>
  <div class="abs hero-btn">Read More</div>
</section>

<section>
  <h2 class="abs h-section welcome-title">WELCOME TO OUR SITE</h2>
  <div class="abs welcome-figure" role="img" aria-label="Photo of a smiling fitness trainer with arms folded"></div>
  <p class="abs welcome-copy">The Riverside Community Academy for the Arts and Technology provides gifted and talented students a differentiated and rigorous education, cultivates a supportive environment that inspires unique artistic and technological visions, promotes cultural tolerance, nurtures community partnerships, and produces active, engaged citizens. Learn More Latin words, consectetur, from a Lorem Ipsum passage, and going through the cites of the word in classical literature,</p>
  <p class="abs welcome-copy2">ary to popular belief, Lorem Ipsum is not simply random text. It has roots in a piece of classical BC, making it over 2000 years old. Martin Hale, a Latin professor at Northbrook College, looked up one of the more obscure Latin words, consectetur, from a Lorem Ipsum passage, and</p>
  <div class="abs video" role="img" aria-label="Video still of an athlete lifting dumbbells">
    <div class="play"><svg width="9" height="9" viewBox="0 0 9 9"><path d="M2 1 L8 4.5 L2 8Z" fill="#fff"/></svg></div>
  </div>
</section>

<section>
  <h2 class="abs h-section col-title" style="left:67px;width:210px">OUR TRAINERS</h2>
  <svg class="abs" style="left:70px;top:742px" width="12" height="20" viewBox="0 0 12 20"><path d="M10 1 L2 10 L10 19" fill="none" stroke="#8ccbe6" stroke-width="1.2"/></svg>
  <svg class="abs" style="left:262px;top:742px" width="12" height="20" viewBox="0 0 12 20"><path d="M2 1 L10 10 L2 19" fill="none" stroke="#8ccbe6" stroke-width="1.2"/></svg>
  <div class="abs trainer" style="left:84px">
    <div class="trainer-photo" role="img" aria-label="Portrait of trainer Clara Weston"></div>
    <div class="trainer-name">CLARA WESTON</div>
    <div class="trainer-role">SPINNING</div>
    <div class="trainer-quote">Creating the perfect body is no small matter.</div>
    <div class="trainer-icons"><svg width="18" height="8" viewBox="0 0 18 8"><path d="M4 7.5 L0.6 4 A2 2 0 0 1 4 1.5 A2 2 0 0 1 7.4 4Z" fill="#d8232a"/><rect x="11" y="2" width="5" height="5" fill="#aaa"/></svg><span><svg width="16" height="8"><circle cx="3" cy="4" r="3" fill="#52b5e0"/><circle cx="12" cy="4" r="3" fill="#52b5e0"/></svg></span></div>
  </div>
  <div class="abs trainer-divider"></div>
  <div class="abs trainer" style="left:181px">
    <div class="trainer-photo" role="img" aria-label="Portrait of trainer Liam Carver" style="background:linear-gradient(180deg,#6a5a50,#c9c4c0)"></div>
    <div class="trainer-name">LIAM CARVER</div>
    <div class="trainer-role">KIK BOXING</div>
    <div class="trainer-quote">Creating the perfect body is no small matter.</div>
    <div class="trainer-icons"><svg width="18" height="8" viewBox="0 0 18 8"><path d="M4 7.5 L0.6 4 A2 2 0 0 1 4 1.5 A2 2 0 0 1 7.4 4Z" fill="#aaa"/><rect x="11" y="2" width="5" height="5" fill="#2a9fd6"/></svg><span><svg width="16" height="8"><circle cx="3" cy="4" r="3" fill="#52b5e0"/><circle cx="12" cy="4" r="3" fill="#52b5e0"/></svg></span></div>
  </div>

  <div class="abs mini-arrow red" style="left:295px;top:659px"><svg width="6" height="6" viewBox="0 0 6 6"><path d="M4 1 L2 3 L4 5" fill="none" stroke="#fff" stroke-width="1.2"/></svg></div>
  <h2 class="abs h-section col-title" style="left:320px;width:162px">NEXT EVENTS</h2>
  <div class="abs mini-arrow" style="left:496px;top:659px"><svg width="6" height="6" viewBox="0 0 6 6"><path d="M2 1 L4 3 L2 5" fill="none" stroke="#fff" stroke-width="1.2"/></svg></div>
  <div class="abs events">
    <div class="event" style="top:10px">
      <div class="event-date">26 GEN, 2014</div>
      <div class="event-photo" role="img" aria-label="Photo of an aerobics class"></div>
      <div class="event-time">h.12.00 - h.13.00</div>
      <div class="event-name">AEROBICS</div>
      <div class="event-text">Lorem ipsum dolor sit amet, consectetur adipiscing elit</div>
      <div class="event-book">BOOKING</div>
    </div>
    <div class="event-rule"></div>
    <div class="event" style="top:78px">
      <div class="event-date">26 GEN, 2014</div>
      <div class="event-photo" role="img" aria-label="Photo of a spinning studio" style="background:linear-gradient(135deg,#dfe6ea,#8f9aa2)"></div>
      <div class="event-time">h.12.00 - h.13.00</div>
      <div class="event-name">SPINNING</div>
      <div class="event-text">Lorem ipsum dolor sit amet, consectetur adipiscing elit</div>
      <div class="event-book">BOOKING</div>
    </div>
  </div>

  <div class="abs mini-arrow" style="left:524px;top:659px"><svg width="6" height="6" viewBox="0 0 6 6"><path d="M4 1 L2 3 L4 5" fill="none" stroke="#fff" stroke-width="1.2"/></svg></div>
  <h2 class="abs col-title" style="left:540px;width:176px;font-size:12px;font-weight:600;color:var(--ink)">FROM THE BLOG</h2>
  <div class="abs mini-arrow" style="left:723px;top:659px"><svg width="6" height="6" viewBox="0 0 6 6"><path d="M2 1 L4 3 L2 5" fill="none" stroke="#fff" stroke-width="1.2"/></svg></div>
  <div class="abs blog">
    <div class="blog-item" style="top:7px"><div class="blog-thumb" role="img" aria-label="Photo of two people jogging" style="background:linear-gradient(180deg,#7fa27a,#c2574a)"></div><div class="blog-text">Lorem ipsum dolor sit amet, consectetur adipiscing elit<div class="blog-date">26 May, 2013</div></div></div>
    <div class="blog-item" style="top:52px"><div class="blog-thumb" role="img" aria-label="Photo of a sprinter in starting position" style="background:linear-gradient(180deg,#2d3d52,#6d7f93)"></div><div class="blog-text">Lorem ipsum dolor sit amet, consectetur adipiscing elit<div class="blog-date">26 May, 2013</div></div></div>
    <div class="blog-item" style="top:96px"><div class="blog-thumb" role="img" aria-label="Photo of a runner at sunset" style="background:linear-gradient(180deg,#d9a45b,#4a3a2a)"></div><div class="blog-text">Lorem ipsum dolor sit amet, consectetur adipiscing elit<div class="blog-date">26 May, 2013</div></div></div>
  </div>
</section>

<section>
  <h2 class="abs h-section partners-title">OUR PARTNERS</h2>
  <div class="abs partner" style="left:67px"><svg width="30" height="30"><rect x="3" y="3" width="24" height="24" fill="#f07a2a"/></svg></div>
  <div class="abs partner" style="left:182px"><svg width="30" height="30"><circle cx="15" cy="15" r="12" fill="#3aa6c8"/></svg></div>
  <div class="abs partner" style="left:297px"><svg width="30" height="30"><circle cx="15" cy="15" r="12" fill="#9c8a6e"/></svg></div>
  <div class="abs partner" style="left:411px"><svg width="30" height="30"><circle cx="15" cy="15" r="12" fill="#c7d52a"/></svg></div>
  <div class="abs partner" style="left:526px"><svg width="30" height="30"><circle cx="15" cy="15" r="12" fill="#f08a1c"/></svg></div>
  <div class="abs partner" style="left:641px"><svg width="30" height="30"><rect x="3" y="3" width="24" height="24" fill="#2a8ecf"/></svg></div>
</section>

<footer>
  <div class="abs footer"></div>
  <h3 class="abs f-head" style="left:68px;top:1023px;font-weight:400">NEWSLETTER SIGNUP</h3>
  <p class="abs f-small" style="left:68px;top:1052px">SIGN UP FOR OUR NEWSLETTER<br>AND GET THE LATEST NEWS.</p>
  <div class="abs f-input">INSERT EMAIL</div>
  <div class="abs f-submit"><span>SUBMIT EMAIL</span><svg width="6" height="8" viewBox="0 0 6 8"><path d="M1 1 L4.5 4 L1 7" fill="none" stroke="#fff" stroke-width="1.3"/></svg></div>

  <div class="abs f-brand"><span class="brand-mark"></span><span class="brand-name">Summit Motion Wellness</span></div>
  <p class="abs f-copy">Lorem ipsum dolor sit amet, consectetur adipiscing elit. Nam viverra euismod odio, gravida pellentesque urna varius vitae. Sed dui lorem, adipiscing in adipiscing et, interdum nec .</p>
  <div class="abs f-contact" style="top:1104px">Phone:<b>1-800-555-0142</b></div>
  <div class="abs f-contact" style="top:1121px">e-mail:<b>hello@summitmotion.example</b></div>

  <h3 class="abs f-head" style="left:552px;top:1023px;font-weight:400">MENU</h3>
  <ul class="abs f-list" style="left:556px;top:1049px"><li>About</li><li>Trainers</li><li>Classes</li><li>Princing</li><li>Privacy</li><li>Contact</li></ul>
  <h3 class="abs f-head" style="left:670px;top:1023px;font-weight:400">COMMUNITY</h3>
  <ul class="abs f-list" style="left:674px;top:1049px"><li>Blog</li><li>Forum</li><li>Support</li><li>Newsletter</li></ul>

  <div class="abs bottom-bar"></div>
  <div class="abs bottom-copy">Copyrights © 2014 summitmotion.example</div>
  <div class="abs social"><span></span><span></span><span></span><span></span><span></span><span></span><span></span></div>
</footer>
</body>
</html>
```